Brisk Fixworks business card

I need business card for my business, I think you have all my details.six months ago I design with you car wrap design. We would like to design both side of the card. On front of card we would like logo , Name and our contact details.
At the back we are looking to mentioned our services.
The name will be:
Gulbadin Norzai
Managing Director
Ph:07955384217
Email:info@brisk-fixworks.com
Web:www.brisk-fixworks.com
So we have our logo, you don’t need to change the logo.
Please see the attachment.
Thanks

Target Market(s)

Home improvement

Industry/Entity Type

Home Improvement

Contact Information for Business Card

Company name: Brisk Fixworks
Name: Gulbadin Norzai
Position: Director
Ph:07955384217
Web: www.brisk-fixworks.com
Add: 14 Garwick Lane
Hounslow
TW3 9QL
SECOND PERSON
Nasrullah norzai
Position: Handyman
Ph: 07822 643157
Email: info@brisk-fixworks.com
Add: 62 Bramcote Vale Drive
Hounslow
TW7 2KD

```html
<!DOCTYPE html>
<html lang="en">
<head>
<meta charset="utf-8">
<title>Brisk Fixworks business card</title>
<link rel="stylesheet" href="https://fonts.googleapis.com/css2?family=Roboto:wght@400;500;700&family=Saira+Semi+Condensed:wght@600&display=swap">
<style>
  :root {
    --navy: #22245f;
    --navy-soft: #3a3d7c;
    --red: #b81f1d;
    --card-light: #f4f4f4;
    --card-shade: #e4e4e6;
    --ink: #2a2a2e;
    --backdrop: #c4c4c6;
  }
  * { box-sizing: border-box; margin: 0; padding: 0; }
  html, body { width: 1200px; height: 576px; overflow: hidden; }
  body {
    background: var(--backdrop);
    font-family: "Roboto", Arial, sans-serif;
    position: relative;
  }
  .card {
    position: absolute;
    width: 484px;
    height: 292px;
    border-radius: 10px;
    overflow: hidden;
    box-shadow: 0 3px 8px rgba(0,0,0,0.25);
  }
  /* Services side */
  .card--services { left: 82px; top: 139px; background: var(--navy); }
  .services-mark {
    position: absolute; left: 0; right: 0; top: 92px;
    display: flex; align-items: center; justify-content: center; gap: 12px;
  }
  .services-mark__square { width: 26px; height: 26px; background: var(--navy-soft); }
  .services-mark__name {
    font-weight: 700; font-size: 34px; color: var(--navy-soft); letter-spacing: 0.5px;
  }
  .services-band {
    position: absolute; left: 0; right: 0; bottom: 0; height: 46px;
    background: var(--red);
    color: #fff; font-size: 13px; line-height: 16px; text-align: center;
    padding-top: 7px;
  }
  /* Contact side */
  .card--contact {
    left: 602px; top: 138px;
    background: linear-gradient(135deg, var(--card-light) 0%, #fafafa 45%, var(--card-shade) 100%);
  }
  .contact-watermark {
    position: absolute; left: 290px; top: 20px; width: 190px; height: 190px;
    border-radius: 50%; background: rgba(34,36,95,0.05);
  }
  .brand {
    position: absolute; left: 22px; top: 56px;
    display: flex; align-items: center; gap: 14px;
  }
  .brand__name { font-weight: 700; font-size: 32px; color: var(--navy); letter-spacing: 0.3px; }
  .brand__square { width: 36px; height: 36px; background: var(--red); }
  .person { position: absolute; left: 23px; top: 192px; }
  .person__name {
    font-family: "Saira Semi Condensed", "Roboto Condensed", sans-serif;
    font-weight: 600; font-size: 20px; color: var(--navy); line-height: 22px;
  }
  .person__role { font-size: 13px; color: var(--ink); margin-top: 2px; }
  .contact-list { position: absolute; left: 258px; top: 180px; list-style: none; }
  .contact-list li {
    display: flex; align-items: center; gap: 9px;
    font-size: 13.5px; color: var(--ink); height: 18.5px;
  }
  .contact-list svg { width: 11px; height: 11px; fill: var(--red); flex: none; }
  .contact-footer { position: absolute; left: 0; bottom: 0; width: 484px; height: 36px; }
  .tagline {
    position: absolute; left: 240px; right: 0; bottom: 11px;
    text-align: center; color: #fff; font-size: 13px;
  }
</style>
</head>
<body>
  <section class="card card--services" aria-label="Card back: services">
    <div class="services-mark">
      <span class="services-mark__square"></span>
      <span class="services-mark__name">Brisk Fixworks</span>
    </div>
    <div class="services-band">
      Electrical&nbsp; | &nbsp;Carpentry&nbsp; | &nbsp;Plumbing&nbsp; | &nbsp;Plastering&nbsp; | &nbsp;Flooring<br>
      Fencing&nbsp; | &nbsp;Decking&nbsp; | &nbsp;Painting &amp; Decorating
    </div>
  </section>

  <section class="card card--contact" aria-label="Card front: contact details">
    <div class="contact-watermark"></div>
    <div class="brand">
      <span class="brand__name">Brisk Fixworks</span>
      <span class="brand__square"></span>
    </div>
    <div class="person">
      <p class="person__name">Gulbadin Norzai</p>
      <p class="person__role">Managing Director</p>
    </div>
    <ul class="contact-list">
      <li><svg viewBox="0 0 12 12"><path d="M1 4c0-1.5 2-2.5 5-2.5S11 2.5 11 4v1H8.5V3.8h-5V5H1zM2.5 6h7l1 4.5h-9z"/></svg>07955384217</li>
      <li><svg viewBox="0 0 12 12"><path d="M0.5 2.5h11v7h-11z M1.2 3l4.8 3.6L10.8 3" stroke="#fff" stroke-width="0.8"/></svg>info@brisk-fixworks.com</li>
      <li><svg viewBox="0 0 12 12"><circle cx="6" cy="6" r="5.2"/><path d="M0.8 6h10.4M6 0.8v10.4M2 3.2h8M2 8.8h8" stroke="#fff" stroke-width="0.7" fill="none"/><ellipse cx="6" cy="6" rx="2.3" ry="5.2" stroke="#fff" stroke-width="0.7" fill="none"/></svg>www.brisk-fixworks.com</li>
    </ul>
    <svg class="contact-footer" viewBox="0 0 484 36" preserveAspectRatio="none">
      <rect x="0" y="26" width="260" height="10" fill="var(--red)"/>
      <path d="M218 0H484V36H194L210 6Q213 0 218 0Z" fill="var(--navy)"/>
    </svg>
    <p class="tagline">Guarantee Arrival on Time</p>
  </section>
</body>
</html>
```